Donations Website - Fund page design

We need an on brand fund page for our crowdfunding website. The design should keep in mind Quillmark Framegrid 3 default columns and spacing.

Please use this development site as a guide... ( under construction )
http://dario.fundquay.example:8080/

Elements to include:
• Framegrid 3 default column layout ( based on 12 column / 1140px / 30px gutters )
• Fund title ( Default Page Fund Title )
• Fund image / video ( 16:9 ratio )
• Fund progress: Current $ amount, Goal $ amount, # donations, # supporters, # views, % progress, progress bar, # shares
• Share buttons ( Chatterbook, Chirply, Vexlo+, WorkMesh, Clipboardy, Email )
• Donate button
• Sections for ( Fund story, fund updates and fund comments... could be tabbed )
• Section for recent donations (name + cb photo / icon + anonymous / donation amount, short message )
• Button to report this fund
• Fund created by section ( name, chatterbook photo if they've verified using chatterbook and number of friends )
• Contact fund raiser button/link
Updates

The design brief has been updated. I've attached the logo as well, please use unless you feel you have something better to include.

Thanks.

I can't stress enough that this is 'NOT' a home page design. This is a personal fund page for a single user. Please do not include 'Other funds' on this page to promote.

Thanks,

Dario

The page should be similar to these pages. As you can see, these are single fund pages within these sites. I do not want my page to look like these, but have the features I included in the brief while fitting my site's design.

http://www.pledgeorbit.example/4kq9zr
https://www.backerloft.example/projects/524190377/lumo-ridge?ref=home_location
http://www.fundhaven.example/projects/the-green-harborites

Thanks,

Dario

Target Market(s)

Adults age 18-50 mainly. Anyone that potentially needs to raise money.

Industry/Entity Type

Construction

Font styles to use
Sans Serif

Colors

Designer to choose colors to be used in the design.

Requirements
Must have
• • Framegrid 3 default column layout ( based on 12 column / 1140px / 30px gutters )
• Donate button
Nice to have
• Would be nice to keep in mind that users may be able to choose a theme color during fund setup. But if the design is strong enough on its own we will not include this option.

```html
<!DOCTYPE html>
<html lang="en">
<head>
<meta charset="utf-8">
<title>First trip to Europe Honeymoon – Fundquay</title>
<link rel="stylesheet" href="https://fonts.googleapis.com/css2?family=Titillium+Web:wght@300;400;600;700&family=Open+Sans:wght@400;600;700&display=swap">
<style>
:root{
  --blue:#1aa0dc;
  --green:#1f6b2f;
  --green-bar:#2e9d3a;
  --orange:#ff6a00;
  --orange-dark:#e85a00;
  --ink:#333;
  --muted:#666;
  --light:#999;
  --line:#ddd;
  --panel:#f2f2f2;
  --link:#1aa0dc;
  --yellow:#f4d21f;
  --dark:#121212;
}
*{box-sizing:border-box;margin:0;padding:0}
html,body{width:758px;height:1200px;overflow:hidden}
body{position:relative;background:#fff;font-family:"Open Sans",sans-serif;color:var(--ink);font-size:8px}
.abs{position:absolute}
h1,h2,.title{font-family:"Titillium Web",sans-serif;font-weight:400}

/* header */
.topbar{left:0;top:0;width:758px;height:34px;background:#fff;border-top:2px solid var(--blue);border-bottom:1px solid #e3e3e3}
.brand{left:80px;top:10px;font:700 11px "Titillium Web",sans-serif;color:var(--green);letter-spacing:.5px;display:flex;align-items:center;gap:4px}
.brand i{width:10px;height:10px;border-radius:50%;background:var(--green);display:block}
.nav{left:176px;top:8px;display:flex}
.nav a{font:600 6px "Open Sans",sans-serif;color:#444;text-transform:uppercase;border:1px solid #ddd;padding:5px 7px;margin-right:4px;text-decoration:none;background:#fff}
.nav a.on{border-color:#ccc;box-shadow:0 1px 2px rgba(0,0,0,.1)}
.btn-signin{left:534px;top:8px;width:42px;height:20px;background:var(--blue);color:#fff;font:600 7px "Open Sans",sans-serif;display:flex;align-items:center;justify-content:center;border-radius:2px}
.btn-create{left:582px;top:8px;width:97px;height:20px;background:var(--green);color:#fff;font:600 7px "Open Sans",sans-serif;display:flex;align-items:center;justify-content:center;border-radius:2px}

/* hero */
.hero{left:0;top:34px;width:758px;height:212px;background:linear-gradient(180deg,#7c6f87 0%,#a886a0 35%,#e6a487 62%,#c06b7a 78%,#5e4a73 100%)}
.created{left:78px;top:88px;display:flex;align-items:center;gap:6px;color:#fff;font:400 8.5px "Titillium Web",sans-serif}
.created .ava{width:20px;height:20px;border-radius:50%;background:#7d6a4a;border:1px solid #fff}
.created b{color:var(--yellow);font-weight:400}
.fund-title{left:78px;top:112px;width:240px;color:#fff;font-size:24px;line-height:26px;font-weight:400}

.stats{left:438px;top:62px;width:241px;height:156px;background:rgba(255,255,255,.92);border-radius:3px;padding:10px 15px}
.amount{font:600 24px "Titillium Web",sans-serif;color:#333;line-height:24px}
.bar{margin-top:4px;height:5px;border-radius:3px;background:var(--green)}
.bar span{display:block;width:78%;height:5px;border-radius:3px;background:var(--green-bar)}
.goal{font-size:6.5px;color:#555;margin-top:3px;padding-bottom:4px;border-bottom:1px solid #ddd}
.nums{display:flex;margin-top:4px}
.nums div{flex:1;font:600 17px "Titillium Web",sans-serif;line-height:18px;color:#333;padding-left:2px}
.nums div+div{border-left:1px solid #ddd;padding-left:12px}
.nums small{display:block;font:400 6.5px "Open Sans",sans-serif;color:#555}
.ends{font-size:6.5px;color:#555;margin-top:5px;padding-top:3px;border-top:1px solid #e4e4e4}
.donate-big{margin-top:5px;height:27px;background:var(--orange);color:#fff;font:600 11px "Open Sans",sans-serif;display:flex;align-items:center;justify-content:center;gap:5px;border-radius:2px}
.notready{text-align:center;font-size:5.5px;color:#444;margin-top:4px}
.notready b{color:var(--orange);font-weight:400}

/* share */
.sharebar{left:0;top:246px;width:758px;height:30px;background:#f4f4f4;border-bottom:1px solid #ddd;border-top:1px solid #e6e6e6}
.share-label{left:79px;top:257px;font:700 7px "Open Sans",sans-serif;color:#333}
.share-items{left:151px;top:246px;display:flex;height:30px}
.share-items div{width:74px;border-left:1px solid #ddd;display:flex;align-items:center;justify-content:center;gap:3px;font-size:7px;color:var(--link)}
.share-items i{width:7px;height:7px;background:var(--link);display:block;border-radius:1px}
.like{background:#4a66a0;color:#fff;font-weight:700;padding:1px 4px;border-radius:1px}
.count{border:1px solid #bbb;color:#777;padding:0 2px;font-size:6px;background:#fff}
.more{left:623px;top:253px;width:42px;height:18px;border:1px solid #ccc;background:#fff;font-size:7px;color:#444;display:flex;align-items:center;justify-content:center}

/* message */
.message{left:0;top:276px;width:758px;height:116px;background:repeating-linear-gradient(135deg,#f1f1f1 0 3px,#ebebeb 3px 6px)}
.msg-ava{left:78px;top:292px;width:44px;height:44px;border-radius:50%;background:#8a8a62}
.msg-from{left:132px;top:302px;font:400 7.5px "Titillium Web",sans-serif;color:#888}
.msg-name{left:132px;top:310px;font:600 15px "Titillium Web",sans-serif;color:#444}
.msg-text{left:132px;top:334px;width:290px;font-size:6.8px;line-height:11px;font-style:italic;color:#777}
.friends-title{left:438px;top:299px;font:400 8.5px "Titillium Web",sans-serif;color:#555}
.friends{left:438px;top:318px;width:232px;display:flex;flex-wrap:wrap;gap:6px}
.friends span{width:26px;height:26px;border-radius:50%;background:#8c7b6a;display:block}
.friends span:nth-child(2n){background:#a58d76}
.friends span:nth-child(3n){background:#5b5f55}

/* story */
h2{font-size:19px;color:#555;line-height:20px}
.story-h{left:79px;top:406px}
.story{left:79px;top:437px;width:344px;font-size:7.6px;line-height:11px;color:#555}
.story p+p{margin-top:11px}
.video{left:438px;top:414px;width:241px;height:135px;border-radius:3px;background:linear-gradient(180deg,#9fb7c8 0%,#b9c2c4 30%,#d6c6a8 62%,#c9b58e 100%)}
.play{left:545px;top:467px;width:26px;height:26px}

.don-h{left:438px;top:562px}
.badge{display:inline-block;font:600 7px "Open Sans",sans-serif;color:#fff;background:#bbb;border-radius:7px;padding:1px 5px;vertical-align:middle;margin-left:4px}
.don{left:438px;width:241px;height:52px}
.don .ava{position:absolute;left:0;top:0;width:26px;height:26px;border-radius:50%;background:#6e5a47}
.don .ago{position:absolute;left:31px;top:1px;font-size:5.8px;color:#888}
.don .who{position:absolute;left:31px;top:7px;font:600 11px "Titillium Web",sans-serif;color:#444}
.don .amt{position:absolute;right:0;top:1px;font:600 18px "Titillium Web",sans-serif;color:#555}
.don .note{position:absolute;left:31px;top:26px;width:210px;font-size:6.5px;line-height:10px;color:#777}
.pager{left:440px;top:772px;display:flex}
.pager span{width:16px;height:16px;border:1px solid #ccc;margin-left:-1px;display:flex;align-items:center;justify-content:center;font-size:6.5px;background:#fff;color:#333}
.pager span.on{background:#ccc}
.donate-now{left:617px;top:772px;width:62px;height:16px;background:var(--orange);color:#fff;font:700 7px "Open Sans",sans-serif;display:flex;align-items:center;justify-content:center;border-radius:1px}

.upd-h{left:79px;top:709px}
.expand{left:370px;top:718px;font-size:8px;color:#555;display:flex;align-items:center;gap:3px}
.expand i{width:8px;height:8px;background:#666;border-radius:1px;color:#fff;font-style:normal;font-size:7px;line-height:8px;text-align:center}
.upd{left:79px;width:344px;display:flex;justify-content:space-between;align-items:baseline}
.upd span{font-size:8.5px;color:#555}
.upd small{font-size:6px;color:#777}

/* testimonials */
.rule{left:0;top:869px;width:682px;height:1px;background:#e5e5e5}
.testi-h{left:79px;top:882px}
.testi{top:910px;width:200px}
.testi .ava{position:absolute;left:0;top:0;width:36px;height:36px;border-radius:50%;background:#a18a72}
.testi .q{position:absolute;left:42px;top:-4px;font:400 18px Georgia,serif;color:#ccc}
.testi p{position:absolute;left:57px;top:2px;width:143px;font-size:6.6px;line-height:10px;color:#333}
.testi .by{position:absolute;left:57px;top:56px;font-size:6.6px;line-height:10px;color:var(--link)}
.testi .qe{position:absolute;left:168px;top:52px;font:400 18px Georgia,serif;color:#ccc}

/* signup */
.signup{left:0;top:1006px;width:758px;height:108px;background:radial-gradient(circle at 50% 40%,#262626 0%,var(--dark) 70%)}
.signup-h{left:79px;top:1026px;width:210px;text-align:right;color:#fff;font-size:19px}
.signup-sub{left:79px;top:1056px;width:210px;text-align:right;color:#666;font-size:6.8px;line-height:12px}
.field{background:#fff;border:1px solid #ddd;border-radius:2px;font-size:8px;color:#777;display:flex;align-items:center;padding-left:10px}
.cur{left:308px;top:1031px;width:64px;height:23px;justify-content:space-between;padding-right:0}
.cur em{width:24px;height:23px;border-left:1px solid #ddd;display:flex;align-items:center;justify-content:center;font-style:normal}
.fund-amt{left:378px;top:1031px;width:160px;height:23px;justify-content:space-between;padding-right:0}
.fund-amt em{width:32px;height:23px;border-left:1px solid #ddd;background:#f5f5f5;display:flex;align-items:center;justify-content:center;font-style:normal;color:#999}
.fund-name{left:308px;top:1060px;width:230px;height:23px}
.fund-btn{left:544px;top:1031px;width:135px;height:52px;background:var(--orange);color:#fff;font:600 11px "Open Sans",sans-serif;display:flex;align-items:center;justify-content:center;border-radius:2px}

/* footer */
.footer{left:0;top:1114px;width:758px;height:86px;background:#f0f0f0}
.foot-links{left:79px;top:1129px;font-size:7px;color:#555;line-height:12px}
.follow{left:513px;top:1129px;display:flex;align-items:center;gap:4px;font-size:7px;color:#555}
.follow span{background:#fff;border:1px solid #ddd;padding:3px 4px;color:#555}
</style>
</head>
<body>

<header class="abs topbar"></header>
<div class="abs brand"><i></i>FUNDQUAY</div>
<nav class="abs nav"><a class="on">How it works</a><a>FAQs</a><a>Support</a><a>About</a></nav>
<div class="abs btn-signin">Sign In</div>
<div class="abs btn-create">Create Your Funraiser</div>

<section class="abs hero" role="img" aria-label="Sunset over water bungalows on a tropical lagoon"></section>
<div class="abs created"><span class="ava" role="img" aria-label="Fund creator photo"></span>Created by: <b>Fund Raiser</b></div>
<h1 class="abs fund-title">First trip to Europe Honeymoon:)</h1>

<aside class="abs stats">
  <div class="amount">$27,118</div>
  <div class="bar"><span></span></div>
  <div class="goal">90% raised of $30k goal</div>
  <div class="nums">
    <div>918<small>Supporters</small></div>
    <div>241<small>Views</small></div>
    <div>15<small>Days</small></div>
  </div>
  <div class="ends">Ends Mar 28, 2014 at 11:59PM PST</div>
  <div class="donate-big">
    <svg width="12" height="12" viewBox="0 0 12 12"><circle cx="6" cy="6" r="6" fill="#fff"/><path d="M6 9.2 3.2 6.5a1.6 1.6 0 0 1 2.3-2.3L6 4.7l.5-.5a1.6 1.6 0 0 1 2.3 2.3Z" fill="#ff6a00"/></svg>
    Make a Donation</div>
  <div class="notready">Not Ready to Donate? <b>Become a Supporter</b></div>
</aside>

<div class="abs sharebar"></div>
<div class="abs share-label">Share this fund:</div>
<div class="abs share-items">
  <div><span class="like">Like</span><span class="count">2.8k</span></div>
  <div><i></i>Share</div>
  <div><i></i>Chirp</div>
  <div><i></i>Clip it</div>
  <div><svg width="8" height="6" viewBox="0 0 8 6"><rect x=".5" y=".5" width="7" height="5" fill="none" stroke="#1aa0dc"/><path d="M.5.5 4 3.5 7.5.5" fill="none" stroke="#1aa0dc"/></svg>Email</div>
  <div><svg width="8" height="8" viewBox="0 0 8 8"><rect width="8" height="8" rx="1" fill="#1aa0dc"/><path d="M3 2 1.5 4 3 6M5 2l1.5 2L5 6" fill="none" stroke="#fff"/></svg>Embed</div>
  <div style="width:0"></div>
</div>
<div class="abs more">More ▾</div>

<section class="abs message"></section>
<div class="abs msg-ava" role="img" aria-label="Profile photo of the fund raiser"></div>
<div class="abs msg-from">A Message From</div>
<div class="abs msg-name">Marcus Ellery</div>
<p class="abs msg-text">Phasellus quam augue, malesuada eu sapien eget, dignissim luctus massa. Aenean rutru igula ligula, nec tincidunt magna luctus id. Sed a sem dignissim, dignissim nunc vel, consectetur risus. Morbi sagittis orci pharetra dolor sagittis egestas.</p>
<div class="abs friends-title">My Chatterbook Friends</div>
<div class="abs friends" role="img" aria-label="Profile photos of eleven Chatterbook friends">
  <span></span><span></span><span></span><span></span><span></span><span></span><span></span>
  <span></span><span></span><span></span><span></span>
</div>

<h2 class="abs story-h">My Story</h2>
<div class="abs story">
  <p>Lorem ipsum dolor sit amet, consectetur adipiscing elit. Vestibulum lectus diam, consequat eget tellus et, faucibus vulputate turpis. Integer commodo dignissim nunc eu rhoncus. Integer at blandit urna. Ut rutrum vitae enim eu aliquam. Ut arcu leo, semper in tempor non, imperdiet eget libero. Nunc lacinia, dui sed adipiscing aliquet, odio tortor blandit enim, eu volutpat libero velit a felis. Nulla tincidunt dapibus metus, pretium suscipit lacus adipiscing at.</p>
  <p>Suspendisse mollis at lacus sed interdum. Vestibulum ante ipsum primis in faucibus orci luctus et ultrices posuere cubilia Curae; Nulla condimentum, neque ac commodo egestas, metus magna facilisis arcu, ac malesuada sapien sapien at purus. Quisque in felis eget sapien laoreet bibendum. Donec rutrum non nunc non molestie. Nullam ut felis sit amet felis varius lacinia. Aenean lacinia orci ac tristique tempor. Phasellus quam augue, malesuada eu sapien eget, dignissim luctus massa. Aenean rutrum ligula ligula, nec tincidunt magna luctus id. Sed a sem dignissim, dignissim nunc vel, consectetur risus. Morbi sagittis orci pharetra dolor sagittis egestas. Integer commodo nec felis et feugiat. Vivamus fringilla facilisis mauris ac iaculis. Nam iaculis laoreet erat, vitae pharetra lectus vestibulum id. Ut non nunc aliquet, faucibus ipsum non, aliquam arcu. Nullam pellentesque purus augue, at posuere arcu porttitor quis.</p>
  <p>Sed nibh leo, pharetra et vulputate a, lobortis quis quam. In egestas nisi at velit sodales fermentum. Nulla lacus nunc, suscipit quis luctus vel, commodo nec sem. Donec blandit elit felis, ut sagittis turpis fringilla bibendum. Suspendisse adipiscing lectus tincidunt ipsum pulvinar, at eleifend erat hendrerit. Nunc pretium egestas velit, in ultrices metus faucibus sit amet. Maecenas ut dapibus ipsum. Vestibulum dapibus tincidunt massa vitae congue. Ut euismod volutpat cursus.</p>
</div>

<div class="abs video" role="img" aria-label="Video still of a smiling couple sitting on a beach"></div>
<svg class="abs play" viewBox="0 0 26 26"><circle cx="13" cy="13" r="12" fill="#fff"/><circle cx="13" cy="13" r="10" fill="#e02020"/><path d="M10.5 8.5v9l7-4.5Z" fill="#fff"/></svg>

<h2 class="abs don-h">Donations <span class="badge">37</span></h2>
<div class="abs don" style="top:596px"><span class="ava" role="img" aria-label="Donor photo"></span><span class="ago">23 Minutes Ago</span><span class="who">Owen Castell</span><span class="amt">$500</span><span class="note">Mira and I really hope this helps out. We know that if it was us that needed to fundraise you'd be right there with your pockets open.</span></div>
<div class="abs don" style="top:654px"><span class="ava" role="img" aria-label="Donor photo"></span><span class="ago">23 Minutes Ago</span><span class="who">Owen Castell</span><span class="amt">$500</span><span class="note">Mira and I really hope this helps out. We know that if it was us that needed to fundraise you'd be right there with your pockets open.</span></div>
<div class="abs don" style="top:710px"><span class="ava" role="img" aria-label="Donor photo"></span><span class="ago">23 Minutes Ago</span><span class="who">Owen Castell</span><span class="amt">$500</span><span class="note">Mira and I really hope this helps out. We know that if it was us that needed to fundraise you'd be right there with your pockets open.</span></div>
<div class="abs pager"><span>1</span><span class="on">2</span><span>3</span><span>4</span><span>5</span></div>
<div class="abs donate-now">Donate Now</div>

<h2 class="abs upd-h">Updates to my fund <span class="badge">3</span></h2>
<div class="abs expand"><i>+</i>Expand All</div>
<div class="abs upd" style="top:747px"><span>Your donations are really helping</span><small>5 minutes ago</small></div>
<div class="abs upd" style="top:768px"><span>Keep it up and I'll hit my goal early!!!</span><small>Tuesday @ 5:38pm</small></div>
<div class="abs upd" style="top:789px"><span>Quick update to let everyone know I'm doing fine</span><small>March 2nd, 2014</small></div>

<div class="abs rule"></div>
<h2 class="abs testi-h">Testimonials</h2>
<div class="abs testi" style="left:79px"><span class="ava" role="img" aria-label="Reviewer photo"></span><span class="q">“</span><p>Intrinsicly evolve just in time web-readiness vis-a-vis sustainable ideas. Progressively restore orthogonal growth strategies and impactful experi-ences. Dynamically .</p><span class="by">Leo Brandwick,<br>NORVALE</span><span class="qe">”</span></div>
<div class="abs testi" style="left:286px"><span class="ava" role="img" aria-label="Reviewer photo"></span><span class="q">“</span><p>Seamlessly myocardinate cross-unit manufactured products whereas intuitive leadership skills. Holisticly develop top-line bandwidth vis-a-vis 2.0 metrics. Compe</p><span class="by">Leo Brandwick,<br>NORVALE</span><span class="qe">”</span></div>
<div class="abs testi" style="left:496px"><span class="ava" role="img" aria-label="Reviewer photo"></span><span class="q">“</span><p>Holisticly expedite corporate band-width whereas virtual results. Distinc-tively synergize web-enabled e-business rather than enterprise-wide results. Continually</p><span class="by">Leo Brandwick,<br>NORVALE</span><span class="qe">”</span></div>

<section class="abs signup"></section>
<h2 class="abs signup-h">Sign Up Now, It's Free!</h2>
<p class="abs signup-sub">For our plunge into married life, Kenji and I are attempting the world's deepest underwater wedding on September 30, 2</p>
<div class="abs field cur">USD<em>▾</em></div>
<div class="abs field fund-amt">Enter fund ammount<em>.00</em></div>
<div class="abs field fund-name">Giver your fund title....</div>
<div class="abs fund-btn">FUND YOUR DREAM</div>

<footer class="abs footer"></footer>
<div class="abs foot-links">Home · Press · FAQ · Blog · Terms · Privacy<br>© 2014 Pledgenest.example</div>
<div class="abs follow">Follow Us On: <span>Chirply</span><span>Chatterbook</span><span>WorkMesh</span><span>Vexlo+</span><span>Clipboardy</span></div>

</body>
</html>
```